K&T Holdings

Design a modern simple business card. I have attached a clean version of a card we like form Marrowfield Partners another company we own. I also attached the old K&T card design and logo and a couple of ideas we had but just can't finalize on whether we like them or not. We would like to include the 20 year logo somewhere on the card.

```html
<!DOCTYPE html>
<html lang="en">
<head>
<meta charset="utf-8">
<title>K&amp;T Holdings – Business Card</title>
<link href="https://fonts.googleapis.com/css2?family=Manrope:wght@400;500;600;700;800&display=swap" rel="stylesheet">
<style>
  :root {
    --navy: #2b2667;
    --grey: #7d7d80;
    --card: #ffffff;
    --page: #f4f4f5;
    --shadow: rgba(0, 0, 0, 0.22);
  }
  * { box-sizing: border-box; margin: 0; padding: 0; }
  html, body { width: 910px; height: 1200px; overflow: hidden; }
  body {
    background: var(--page);
    font-family: "Manrope", Arial, sans-serif;
    display: flex;
    flex-direction: column;
    align-items: center;
    justify-content: center;
    gap: 80px;
  }
  .card {
    width: 620px;
    height: 355px;
    background: var(--card);
    box-shadow: 0 3px 8px var(--shadow);
    position: relative;
    display: flex;
    align-items: center;
  }
  .wordmark {
    font-weight: 800;
    font-size: 84px;
    letter-spacing: -2px;
    color: var(--navy);
    line-height: 1;
  }

  /* Front */
  .card--front { justify-content: center; gap: 36px; }
  .divider { width: 2px; height: 162px; background: var(--navy); }
  .anniversary-mark {
    width: 168px;
    height: 124px;
    background: linear-gradient(180deg, var(--navy) 0%, var(--navy) 58%, var(--grey) 100%);
  }

  /* Back */
  .card--back { padding-left: 62px; }
  .card--back .wordmark { width: 268px; }
  .contact { margin-left: 0; }
  .contact__name { font-size: 28px; font-weight: 600; color: var(--grey); letter-spacing: 0.2px; line-height: 1.1; white-space: nowrap; }
  .contact__title { font-size: 17px; font-weight: 500; color: var(--navy); margin-top: 3px; }
  .contact__list { list-style: none; margin-top: 28px; display: flex; flex-direction: column; gap: 18px; }
  .contact__item { display: flex; align-items: flex-start; gap: 11px; font-size: 13px; color: var(--navy); line-height: 1.3; max-width: 250px; }
  .contact__icon { flex: none; width: 21px; height: 21px; }
</style>
</head>
<body>

  <section class="card card--front" aria-label="Card front">
    <div class="wordmark">K&amp;T</div>
    <div class="divider"></div>
    <div class="anniversary-mark" role="img" aria-label="20 years anniversary mark, 2004 to 2024"></div>
  </section>

  <section class="card card--back" aria-label="Card back">
    <div class="wordmark">K&amp;T</div>
    <div class="contact">
      <p class="contact__name">DANA WHITFIELD</p>
      <p class="contact__title">IT Director</p>
      <ul class="contact__list">
        <li class="contact__item">
          <svg class="contact__icon" viewBox="0 0 20 20" aria-hidden="true"><circle cx="10" cy="10" r="10" fill="#7d7d80"/><path d="M10 4.5a3.5 3.5 0 0 0-3.5 3.5c0 2.6 3.5 6.5 3.5 6.5s3.5-3.9 3.5-6.5A3.5 3.5 0 0 0 10 4.5z" fill="#fff"/><circle cx="10" cy="8" r="1.3" fill="#7d7d80"/></svg>
          <span>812 Cedar Avenue, Suite 410, Millbrook, TX 75500</span>
        </li>
        <li class="contact__item">
          <svg class="contact__icon" viewBox="0 0 20 20" aria-hidden="true"><circle cx="10" cy="10" r="10" fill="#7d7d80"/><rect x="5" y="6.5" width="10" height="7" rx="1" fill="#fff"/><path d="M5.5 7l4.5 3.5L14.5 7" stroke="#7d7d80" stroke-width="1" fill="none"/></svg>
          <span>dwhitfield@ktholdings.com</span>
        </li>
        <li class="contact__item">
          <svg class="contact__icon" viewBox="0 0 20 20" aria-hidden="true"><circle cx="10" cy="10" r="10" fill="#7d7d80"/><path d="M7 5l2 2.5-1.2 1.3a6 6 0 0 0 3.4 3.4l1.3-1.2L15 13l-1 1.8c-4.5 0-8.8-4.3-8.8-8.8z" fill="#fff"/></svg>
          <span>555-204-7319</span>
        </li>
        <li class="contact__item">
          <svg class="contact__icon" viewBox="0 0 20 20" aria-hidden="true"><circle cx="10" cy="10" r="10" fill="#7d7d80"/><rect x="7" y="4.5" width="6" height="11" rx="1" fill="#fff"/><circle cx="10" cy="13.6" r="0.7" fill="#7d7d80"/></svg>
          <span>555-386-0148</span>
        </li>
      </ul>
    </div>
  </section>

</body>
</html>
```